A6 Advertising Post Card

I am looking for refinement on this idea for an advertising letter-box drop of an A6 postcard.
Side 1 - our brand, the address, "15% discount if you present this card before Dec 31"

We are a new retail concept in terms of the store concept.

Side 2 - i want to highlight where the products are from, what materials are used, emphasis on cool, fresh, different, affordable, the product ranges grouped by colours (storage &organisation items in 1 colour or font, illumination products in 1 colour or font, furniture in 1 colour or font, decor in 1 colour or font, curios is 1 colour or font, fasion in 1 colour or font, others in a 1 colour or font)

The Product Categories:
see attachment

Hi

I've added the product categories with products sorted under each heading. I have also added the logo in a variety of file types (jpg, tif, psd, png). The sky blue background is part of the brand image.
Thanks

Target Market(s)

Home-makers (men and women) and women of all ages. Decision makers for home furnishings. Cross demographic - this is not premium..affordable to all social strata.
The brand is about fun, colourful and functional home stuff. The fashion stuff is a small percentage of the overall offer - targeting women who should spoil themselves as they spoil their families with nice stuff for the home.

Industry/Entity Type

Advertising

```html
<!DOCTYPE html>
<html lang="en">
<head>
<meta charset="utf-8">
<title>Kapok – Postcard</title>
<link rel="stylesheet" href="https://fonts.googleapis.com/css2?family=Comic+Neue:wght@400;700&display=swap">
<style>
  :root {
    --sky: #00f5ea;
    --brand: #ff3b12;
    --plum: #5b1a72;
    --violet: #9a00d8;
    --indigo: #4a2a9c;
    --sun: #ffff00;
    --lilac: #9a4dff;
    --diamond: #6f7d95;
    --diamond-edge: #2e3440;
    --backdrop: #ffffff;
  }
  * { margin: 0; padding: 0; box-sizing: border-box; }
  html, body {
    width: 1200px;
    height: 883px;
    overflow: hidden;
    background: var(--backdrop);
  }
  .postcard {
    position: relative;
    width: 1200px;
    height: 883px;
    background: var(--sky);
    font-family: "Comic Neue", "Comic Sans MS", cursive;
    overflow: hidden;
  }
  .brand-name {
    position: absolute;
    left: 0;
    right: 0;
    top: 40px;
    text-align: center;
    font-size: 330px;
    font-weight: 700;
    line-height: 1;
    color: var(--brand);
  }
  .tagline {
    position: absolute;
    left: 0;
    right: 0;
    top: 512px;
    display: flex;
    justify-content: center;
    align-items: center;
    gap: 36px;
    font-size: 70px;
    line-height: 1;
    color: var(--plum);
  }
  .tagline .divider {
    width: 38px;
    height: 38px;
    margin-top: 10px;
  }
  .offer-band {
    position: absolute;
    left: 28px;
    top: 630px;
    width: 1144px;
    height: 97px;
  }
  .offer-band svg {
    position: absolute;
    inset: 0;
  }
  .offer-text {
    position: absolute;
    inset: 0;
    display: flex;
    align-items: center;
    justify-content: center;
    font-size: 47px;
    font-weight: 700;
    line-height: 1;
    color: var(--violet);
  }
  .store-line {
    position: absolute;
    left: 0;
    right: 0;
    top: 764px;
    text-align: center;
    font-size: 50px;
    line-height: 1;
    color: var(--indigo);
  }
  .scallop-edge {
    position: absolute;
    left: 0;
    bottom: 0;
    width: 1200px;
    height: 50px;
  }
</style>
</head>
<body>
  <main class="postcard">
    <h1 class="brand-name">Kapok</h1>

    <p class="tagline">
      <span>home</span>
      <svg class="divider" viewBox="0 0 36 36" aria-hidden="true">
        <polygon points="18,2 34,18 18,34 2,18" fill="var(--diamond)" stroke="var(--diamond-edge)" stroke-width="1.5"/>
      </svg>
      <span>gifts</span>
    </p>

    <div class="offer-band">
      <svg width="1144" height="97" viewBox="0 0 1144 97" aria-hidden="true">
        <defs>
          <filter id="band-shadow" x="-5%" y="-20%" width="110%" height="150%">
            <feDropShadow dx="2" dy="3" stdDeviation="2" flood-color="#000" flood-opacity="0.35"/>
          </filter>
        </defs>
        <g fill="var(--sun)" filter="url(#band-shadow)">
          <rect x="48" y="8" width="1048" height="81"/>
          <circle cx="48" cy="48.5" r="47"/><circle cx="112" cy="48.5" r="47"/>
          <circle cx="176" cy="48.5" r="47"/><circle cx="240" cy="48.5" r="47"/>
          <circle cx="304" cy="48.5" r="47"/><circle cx="368" cy="48.5" r="47"/>
          <circle cx="432" cy="48.5" r="47"/><circle cx="496" cy="48.5" r="47"/>
          <circle cx="560" cy="48.5" r="47"/><circle cx="624" cy="48.5" r="47"/>
          <circle cx="688" cy="48.5" r="47"/><circle cx="752" cy="48.5" r="47"/>
          <circle cx="816" cy="48.5" r="47"/><circle cx="880" cy="48.5" r="47"/>
          <circle cx="944" cy="48.5" r="47"/><circle cx="1008" cy="48.5" r="47"/>
          <circle cx="1050" cy="48.5" r="47"/><circle cx="1096" cy="48.5" r="47"/>
        </g>
      </svg>
      <p class="offer-text">15% discount if you present this card before Dec 31</p>
    </div>

    <p class="store-line">A new store concept at 42 Fern Street, Linwood</p>

    <svg class="scallop-edge" viewBox="0 0 1200 50" aria-hidden="true">
      <g fill="var(--lilac)">
        <rect x="0" y="30" width="1200" height="20"/>
        <circle cx="0" cy="36" r="34"/><circle cx="68" cy="36" r="34"/>
        <circle cx="136" cy="36" r="34"/><circle cx="204" cy="36" r="34"/>
        <circle cx="272" cy="36" r="34"/><circle cx="340" cy="36" r="34"/>
        <circle cx="408" cy="36" r="34"/><circle cx="476" cy="36" r="34"/>
        <circle cx="544" cy="36" r="34"/><circle cx="612" cy="36" r="34"/>
        <circle cx="680" cy="36" r="34"/><circle cx="748" cy="36" r="34"/>
        <circle cx="816" cy="36" r="34"/><circle cx="884" cy="36" r="34"/>
        <circle cx="952" cy="36" r="34"/><circle cx="1020" cy="36" r="34"/>
        <circle cx="1088" cy="36" r="34"/><circle cx="1156" cy="36" r="34"/>
        <circle cx="1224" cy="36" r="34"/>
      </g>
    </svg>
  </main>
</body>
</html>
```